43 Year Old Construction firm needs Updated Business Card & Stationery Design

We are an established and well known (in our market) commercial construction firm. We need a cleaner and more modern look for our corporate identity material. We would like to continue to use our current colors and logo.
We are thinking about incorporating a slogan on our business card (either front or back): "Striving to be the most trusted builder in our market." The text could change at some point. Our website is www.kradworth.example . Sample card is attached. Some will have more phone numbers, etc...
Updates

Target Market(s)

Commercial and institutional clients.

Industry/Entity Type

Construction Company

Contact Information for Business Card

See attached for existing card. But don't be constrained.

Requirements
Must have
• Logo, name, title, address, website, email, phone numbers (as few as one, as many as three)
• Slogan on front or back "Striving to be the most trusted builder in our market"
• Use existing logo and colors

```html
<!DOCTYPE html>
<html lang="en">
<head>
<meta charset="utf-8">
<title>Kradworth Builders — Stationery Set</title>
<link href="https://fonts.googleapis.com/css2?family=Lato:wght@400;700;900&display=swap" rel="stylesheet">
<style>
:root{
  --navy:#123f80;
  --navy-deep:#0d3370;
  --navy-light:#2a5fa8;
  --green:#1f8a45;
  --paper:#ffffff;
  --ink:#2b2f3a;
  --muted:#6a6f7a;
  --backdrop:#d4d4d6;
}
*{margin:0;padding:0;box-sizing:border-box}
html,body{width:1200px;height:2253px;overflow:hidden}
body{background:var(--backdrop);font-family:"Lato",Arial,sans-serif;color:var(--ink);position:relative}
.piece{position:absolute;background:var(--paper);overflow:hidden}

/* brand name lockup */
.brand{display:flex;align-items:center;gap:6px;font-weight:900;letter-spacing:.04em;color:var(--navy);white-space:nowrap}
.brand .mark{display:block;background:var(--navy)}
.brand.on-dark{color:#fff}
.brand.on-dark .mark{background:#fff}

.web-tag{position:absolute;right:12px;bottom:0;background:var(--green);color:#fff;font-weight:700;white-space:nowrap}
.base-bar{position:absolute;left:0;right:0;bottom:0;background:var(--navy)}

/* letterhead */
.letterhead{left:213px;top:60px;width:335px;height:443px}
.letterhead .brand{position:absolute;left:26px;top:22px;font-size:14px}
.letterhead .brand .mark{width:12px;height:12px}
.sheet-contact{position:absolute;right:26px;top:22px;font-size:5.5px;line-height:7px;color:var(--muted)}
.letter-body{position:absolute;left:36px;top:124px;width:262px;font-size:5px;line-height:6.6px;color:var(--muted)}
.letter-body p{margin-bottom:6px}
.letter-body .date,.letter-body .signer{font-weight:700;color:var(--ink)}
.letter-body .recipient{margin-bottom:8px}
.letterhead .base-bar{height:8px}
.letterhead .web-tag{font-size:5px;padding:2px 5px;bottom:0}

/* folder inner */
.folder-inner{left:585px;top:60px;width:353px;height:443px}
.folder-inner .brand{position:absolute;left:26px;top:22px;font-size:14px}
.folder-inner .brand .mark{width:12px;height:12px}
.folder-inner svg{position:absolute;left:0;bottom:0}

/* business cards */
.card-front{left:204px;top:541px;width:354px;height:211px}
.card-front .brand{position:absolute;right:18px;top:20px;font-size:17px}
.card-front .brand .mark{width:13px;height:13px}
.card-name{position:absolute;left:16px;top:108px;font-size:13px;font-weight:700;color:var(--navy)}
.card-title{position:absolute;left:16px;top:125px;font-size:10px;color:var(--ink)}
.card-contact{position:absolute;left:16px;top:162px;font-size:10px;line-height:14px}
.card-contact b{color:var(--navy)}
.card-address{position:absolute;right:16px;top:162px;font-size:10px;line-height:14px;text-align:right}
.card-front .base-bar{height:10px}
.card-front .web-tag{font-size:8px;padding:2px 7px}

.card-back{left:579px;top:541px;width:356px;height:211px;background:radial-gradient(ellipse at 50% 45%,var(--navy-light),var(--navy-deep) 75%);display:flex;align-items:center;justify-content:center}
.card-back .brand{font-size:24px}
.card-back .brand .mark{width:18px;height:18px}

/* envelope */
.envelope-front{left:204px;top:775px;width:731px;height:315px}
.envelope-front .brand{position:absolute;left:33px;top:30px;font-size:24px}
.envelope-front .brand .mark{width:18px;height:18px}
.envelope-address{position:absolute;left:33px;top:100px;font-size:11px;line-height:13px;color:var(--ink)}
.envelope-front .base-bar{height:22px}
.envelope-front .web-tag{font-size:11px;padding:4px 9px;bottom:2px;right:40px}

.envelope-back{left:204px;top:1126px;width:731px;height:314px}
.envelope-back svg{position:absolute;left:0;top:0}
.envelope-back .brand{position:absolute;left:50%;top:42px;transform:translateX(-50%);font-size:22px}
.envelope-back .brand .mark{width:16px;height:16px}

/* presentation folder cover */
.folder-cover{left:330px;top:1490px;width:540px;height:730px;background:linear-gradient(180deg,var(--navy-deep) 0%,var(--navy) 55%,var(--navy-light) 100%)}
.folder-cover .brand{position:absolute;left:50%;top:120px;transform:translateX(-50%);font-size:38px}
.folder-cover .brand .mark{width:26px;height:26px}
.folder-cover .cover-web{position:absolute;left:50%;bottom:40px;transform:translateX(-50%);color:#fff;font-size:14px;letter-spacing:.04em;opacity:.9}
</style>
</head>
<body>

<section class="piece letterhead" aria-label="Letterhead">
  <div class="brand"><span class="mark"></span>KRADWORTH</div>
  <div class="sheet-contact">
    <div>&#9742; 555.010.4562</div>
    <div>&#9742; 555.010.7310</div>
    <div>&#9993; danw@kradworth.example</div>
    <div>4120 Fieldstone Avenue</div>
    <div>Millbrook, MO 63000</div>
  </div>
  <div class="letter-body">
    <p class="date">12 May 2024</p>
    <p class="recipient">Mr. Jonathan<br>Human Resource Manager<br>Northgate Design Studio<br>18 Elm Street, Millbrook</p>
    <p>Dear Sir/Madam</p>
    <p>Thank you for your recent inquiry about our commercial building services. We are pleased to share an overview of our team, our recent projects and the way we plan, schedule and deliver work for institutional clients.</p>
    <p>Our project managers stay on site from groundbreaking to final handover, keeping budgets clear and progress visible at every stage.</p>
    <p>We would welcome the chance to meet with you and discuss your plans in more detail at a time that suits you.</p>
    <p>Yours Sincerely</p>
    <p class="signer">Daniel R. Whitcombe<br><span style="font-weight:400;color:var(--muted)">Marketing Manager<br>Millbrook Office</span></p>
  </div>
  <div class="base-bar"></div>
  <div class="web-tag">www.kradworth.example</div>
</section>

<section class="piece folder-inner" aria-label="Folder inner pocket">
  <div class="brand"><span class="mark"></span>KRADWORTH</div>
  <div class="sheet-contact">
    <div>&#9742; 555.010.4562</div>
    <div>&#9742; 555.010.7310</div>
    <div>&#9993; danw@kradworth.example</div>
    <div>4120 Fieldstone Avenue</div>
    <div>Millbrook, MO 63000</div>
  </div>
  <svg width="353" height="200" viewBox="0 0 353 200">
    <path d="M80 200 C80 150 105 130 150 115 L353 0 L353 200 Z" fill="var(--navy)"/>
  </svg>
</section>

<section class="piece card-front" aria-label="Business card front">
  <div class="brand"><span class="mark"></span>KRADWORTH</div>
  <div class="card-name">Daniel R. Whitcombe</div>
  <div class="card-title">President</div>
  <div class="card-contact">
    <div><b>D:</b> 555.010.4562</div>
    <div><b>E:</b> danw@kradworth.example</div>
  </div>
  <div class="card-address">
    <div>4120 Fieldstone Avenue</div>
    <div>Millbrook, MO 63000</div>
  </div>
  <div class="base-bar"></div>
  <div class="web-tag">www.kradworth.example</div>
</section>

<section class="piece card-back" aria-label="Business card back">
  <div class="brand on-dark"><span class="mark"></span>KRADWORTH</div>
</section>

<section class="piece envelope-front" aria-label="Envelope front">
  <div class="brand"><span class="mark"></span>KRADWORTH</div>
  <div class="envelope-address">
    <div>4120 Fieldstone Avenue</div>
    <div>Millbrook, MO 63000</div>
  </div>
  <div class="base-bar"></div>
  <div class="web-tag">www.kradworth.example</div>
</section>

<section class="piece envelope-back" aria-label="Envelope back">
  <svg width="731" height="130" viewBox="0 0 731 130">
    <path d="M0 0 H731 V40 L700 105 Q690 124 668 124 H63 Q41 124 31 105 L0 40 Z" fill="var(--navy)"/>
  </svg>
  <div class="brand on-dark"><span class="mark"></span>KRADWORTH</div>
</section>

<section class="piece folder-cover" aria-label="Presentation folder cover">
  <div class="brand on-dark"><span class="mark"></span>KRADWORTH</div>
  <div class="cover-web">www.kradworth.example</div>
</section>

</body>
</html>
```